Online Digital Solutions Agency needs a New Business Card

We are a Online/Digital solution agency. We provide WordPress Solutions, Online & Digital Marketing Solutions including SEO, Social Media Marketing and Managed Hosting including VPS and Cloud Hosting solutions. We also design and build bespoke web sites and web applications for various clients. We are very good at site migrations, 3rd party API integrations and mobile app development.

We are rebranding our agency and have already designed a new logo. We have selected 5-6 colours as our base colour and are currently building our new website based around these colour scheme.

Our logo indicates that we are a cloud solution providers, and (i.e. the Clouds), and developers (i.e. HTML Tags, and CSS formats). We use the 5-6 base colours and use various shades of these colours as required.

Our old website is located at: www.brambleforgelabs.com

And our new website is going to be at (we are working on it at the moment ...):
https://creative.brambleforgelabs.co.uk/

Our slogan is "Digital Transformation Specialist"

What we mean by that is; we can take any existing business and get them up and transform them in to the digital world, starting with Hosting, Web Design, Development & Online Marketing aspects.

The powerpoint is a document that we use to present our projects to clients at the moment, and the cloud is on the background as we clarified earlier. (Just to get the idea)

What we are looking for is a Great WoW factor design to start with, ideally with the Logo and Logo colour scheme if possible but not required as long as the designers can do better, and basically give life to our logo and company via the Business card design.

Ideally with some icons perhaps to indicate the address, location, mobile, email, and website would be good but again optional as long as there is a good design.

The cloud can be used as a background if required in a light shade or as a watermark share perhaps.

The logos' and the Illustrator files are shared with you so you can use them as required.

Ideally the business card should have a Name, title, Mobile, Email , Website, Address and perhaps some social media links.

Target Market(s)

New Startups, SME's, Contract and Outsource Clients

Contact Information for Business Card

Company Name:
==============
BrambleForge Labs (UK) Ltd.

Tag Line:
========
“Digital Transformation Specialists”

Adress:
=======

Suite KR73054
14-16 Ashgrove Lane
London
E9 4PD.

Name:
=====
Idris Malek

Title: (Optional)
=============
FQTA, PgD (RNOM)

Role:
=====
Digital Solutions Architect

Email:
=====
idris@brambleforgelabs.uk

WebSite:
=======
http://www.brambleforgelabs.uk

OR

www.brambleforgelabs.uk

Mobile:
======
0044 (0)75 218 30479

OR

+44 (0)75 218 30479

LinkedIN: (Optional)
========
https://uk.linkedin.com/in/idrismalek

Skype: (Optional)
======
idris.malek

Twitter (Optional) : idrismalek

Font styles to use
Serif
Sans Serif

Requirements
Must have
• The Logo
• Business Name
• Person Name
• Title
• Mobile
• Email
• Website
• Address
• I have provided the colour scheme on my files.
Nice to have
• Twiter
• Linked in
• Facebook

```html
<!DOCTYPE html>
<html lang="en">
<head>
<meta charset="utf-8">
<title>BrambleForge Labs – Business Card</title>
<link rel="stylesheet" href="https://fonts.googleapis.com/css2?family=Roboto:wght@400;500;700;900&display=swap">
<style>
  :root {
    --stage: #434446;
    --teal-light: #55bfd6;
    --teal-dark: #2b97a8;
    --brand-blue: #1a4f9c;
    --brand-cyan: #27a9c8;
    --accent-orange: #f2a51a;
    --ink: #1d1d1f;
    --white: #ffffff;
  }
  * { box-sizing: border-box; margin: 0; padding: 0; }
  html, body { width: 1200px; height: 874px; overflow: hidden; }
  body {
    background: var(--stage);
    font-family: "Roboto", sans-serif;
    position: relative;
  }
  .card {
    position: absolute;
    width: 560px;
    height: 320px;
    border-radius: 22px;
    overflow: hidden;
    box-shadow: 0 14px 30px rgba(0,0,0,.35);
  }

  /* Front */
  .card-front {
    left: 60px; top: 70px;
    background: linear-gradient(180deg, var(--teal-light), var(--teal-dark));
    color: var(--white);
    display: flex; flex-direction: column; align-items: center; justify-content: center;
    text-align: center;
  }
  .card-front .brand-name {
    font-weight: 900; font-size: 46px; color: var(--brand-blue); letter-spacing: -.5px;
  }
  .card-front .tagline { font-size: 17px; letter-spacing: 1px; margin-top: 6px; }
  .social-row { display: flex; align-items: center; gap: 6px; margin-top: 22px; font-size: 15px; letter-spacing: .5px; }
  .social-dot { width: 16px; height: 16px; border-radius: 50%; background: var(--white); }
  .social-row .handle { margin-left: 6px; }

  /* Back */
  .card-back {
    left: 580px; top: 480px;
    background: var(--white);
    color: var(--ink);
  }
  .back-logo { position: absolute; left: 40px; top: 70px; }
  .back-logo .brand-name { font-weight: 900; font-size: 34px; color: var(--brand-blue); letter-spacing: -.5px; }
  .back-logo .tagline { font-size: 14px; margin-top: 4px; letter-spacing: .5px; }

  .identity { position: absolute; right: 30px; top: 40px; text-align: right; }
  .identity .person { font-weight: 900; font-size: 30px; color: var(--brand-blue); }
  .identity .role { font-size: 14px; margin-top: 2px; }
  .identity .rule { height: 1.5px; background: var(--accent-orange); width: 250px; margin: 12px 0 10px auto; }
  .identity .company { font-size: 14px; color: var(--brand-cyan); }
  .identity .address { font-size: 14px; line-height: 1.35; }

  .contact-rule { position: absolute; left: 40px; top: 212px; width: 240px; height: 1.5px; background: var(--accent-orange); }
  .contact-list { position: absolute; left: 40px; top: 222px; list-style: none; font-size: 14px; }
  .contact-list li { display: flex; align-items: center; gap: 10px; height: 22px; }
  .contact-list svg { width: 13px; height: 13px; fill: var(--brand-blue); }

  .base-band { position: absolute; left: 0; bottom: 0; width: 100%; height: 10px; display: flex; }
  .base-band .band-teal { flex: 0 0 62%; background: var(--brand-cyan); }
  .base-band .band-blue { flex: 1; background: var(--brand-blue); }
</style>
</head>
<body>

<section class="card card-front" aria-label="Card front">
  <div class="brand-name">BrambleForge Labs</div>
  <div class="tagline">Digital Transformation Specialist</div>
  <div class="social-row">
    <span class="social-dot"></span><span class="social-dot"></span><span class="social-dot"></span>
    <span class="handle">idrismalek</span>
  </div>
</section>

<section class="card card-back" aria-label="Card back">
  <div class="back-logo">
    <div class="brand-name">BrambleForge Labs</div>
    <div class="tagline">Digital Transformation Specialist</div>
  </div>

  <div class="identity">
    <div class="person">Idris Malek</div>
    <div class="role">Digital Solutions Architect</div>
    <div class="rule"></div>
    <div class="company">BrambleForge Labs (UK) Ltd</div>
    <div class="address">14-16, Ashgrove Lane, London<br>E9 4PD, United Kingdom</div>
  </div>

  <div class="contact-rule"></div>
  <ul class="contact-list">
    <li><svg viewBox="0 0 24 24"><path d="M6.6 10.8a15 15 0 0 0 6.6 6.6l2.2-2.2c.3-.3.7-.4 1-.2 1.1.4 2.3.6 3.6.6.6 0 1 .4 1 1V20c0 .6-.4 1-1 1C10.6 21 3 13.4 3 4c0-.6.4-1 1-1h3.5c.6 0 1 .4 1 1 0 1.3.2 2.5.6 3.6.1.3 0 .7-.2 1z"/></svg>+44 (0)75 218 30479</li>
    <li><svg viewBox="0 0 24 24"><path d="M2 5h20v14H2z M2 5l10 8 10-8" fill="none" stroke="#1a4f9c" stroke-width="2"/></svg>idris@brambleforgelabs.uk</li>
    <li><svg viewBox="0 0 24 24"><circle cx="12" cy="12" r="9" fill="none" stroke="#1a4f9c" stroke-width="2"/><path d="M3 12h18M12 3c3 3 3 15 0 18M12 3c-3 3-3 15 0 18" fill="none" stroke="#1a4f9c" stroke-width="1.5"/></svg>www.brambleforgelabs.uk</li>
  </ul>

  <div class="base-band"><span class="band-teal"></span><span class="band-blue"></span></div>
</section>

</body>
</html>
```